Real Estate "For Sale" Sign for construction company

We need a sign that we can use to hang on a post and place on the road when we sell a property. The sign will be simple and will need to mainly feature our logo (files attached), as well as the words "For Sale", and then our phone number "(555) 617 3489". The sign will hang on a post that'll look something like the attached picture.

Target Market(s)

Home buyers

Industry/Entity Type

Real Estate

Font styles to use
Serif
Sans Serif

Colors
0054AA
0677BA
7BADD7
CADEEF
E8F1F8
0094D4
00A9DD
6FCCEA
C7EBF8
E9F6FB

Requirements
Must have
• For Sale & our phone number

```html
<!DOCTYPE html>
<html lang="en">
<head>
<meta charset="utf-8">
<title>For Sale Sign – Ridgeline Valley Homes</title>
<link rel="stylesheet" href="https://fonts.googleapis.com/css2?family=Archivo:wght@400;700&family=Oswald:wght@700&display=swap">
<style>
  :root {
    --page-bg: #f5f6f8;
    --ink: #3d4a6e;
    --ink-deep: #36446a;
    --brand-blue: #3a8fcf;
    --sky-1: #e6f4fc;
    --sky-2: #f6fbfe;
    --line-light: #6fccea;
    --line-mid: #3f6fae;
    --line-dark: #3d4a6e;
  }
  * { box-sizing: border-box; margin: 0; padding: 0; }
  html, body {
    width: 1200px; height: 1200px; overflow: hidden;
    background: var(--page-bg);
  }
  .sign {
    position: absolute; left: 183px; top: 20px;
    width: 834px; height: 1160px;
    background: linear-gradient(100deg, #ffffff 0%, var(--sky-2) 50%, var(--sky-1) 100%);
    overflow: hidden;
  }
  .sign__top-panel { position: absolute; inset: 0; }
  .sign__edge {
    position: absolute; left: 0; right: 0; height: 3px;
  }
  .sign__edge--top { top: 0; background: linear-gradient(90deg, var(--line-light) 0 33%, var(--line-mid) 33% 67%, var(--line-dark) 67%); }
  .sign__edge--bottom { bottom: 0; background: linear-gradient(90deg, var(--line-dark) 0 33%, var(--line-mid) 33% 67%, var(--line-light) 67%); }
  .sign__headline {
    position: absolute; left: 0; right: 0; top: 186px;
    text-align: center;
    font-family: "Archivo", sans-serif; font-weight: 700;
    font-size: 114px; line-height: 1; letter-spacing: -0.02em;
    color: var(--ink);
  }
  .sign__cta {
    position: absolute; left: 0; right: 0; top: 345px;
    text-align: center; padding-left: 0.42em;
    font-family: "Archivo", sans-serif; font-weight: 400;
    font-size: 44px; line-height: 1; letter-spacing: 0.42em;
    color: var(--ink);
    white-space: nowrap;
  }
  .sign__phone {
    position: absolute; left: -100px; right: -100px; top: 386px;
    text-align: center; white-space: nowrap;
    font-family: "Oswald", sans-serif; font-weight: 700;
    font-size: 150px; line-height: 1; letter-spacing: -0.01em;
    color: var(--ink-deep);
    transform: scaleX(0.84); transform-origin: 50% 50%;
  }
  .sign__divider {
    position: absolute; left: 199px; width: 437px; top: 669px;
    height: 1.5px; background: var(--ink);
  }
  .brand {
    position: absolute; left: 0; right: 0; top: 905px;
    text-align: center; color: var(--brand-blue);
    font-family: "Archivo", sans-serif; font-weight: 400;
  }
  .brand__name { font-size: 66px; line-height: 1; letter-spacing: -0.01em; white-space: nowrap; }
  .brand__tagline {
    margin-top: 22px; padding-left: 0.9em;
    font-size: 22px; line-height: 1; letter-spacing: 0.9em;
  }
</style>
</head>
<body>
  <main class="sign">
    <svg class="sign__top-panel" width="834" height="1160" viewBox="0 0 834 1160" aria-hidden="true">
      <defs>
        <linearGradient id="topPanelFill" x1="0" y1="0" x2="1" y2="0">
          <stop offset="0" stop-color="#e6f4fc"/>
          <stop offset="0.6" stop-color="#f5fafd"/>
          <stop offset="1" stop-color="#ffffff"/>
        </linearGradient>
      </defs>
      <path d="M0 0 H834 V612 Q830 660 778 690 L417 880 L56 690 Q6 662 0 612 Z" fill="url(#topPanelFill)"/>
    </svg>
    <div class="sign__edge sign__edge--top"></div>
    <h1 class="sign__headline">FOR SALE</h1>
    <p class="sign__cta">CALL US TODAY</p>
    <p class="sign__phone">(555) 617 3489</p>
    <div class="sign__divider"></div>
    <div class="brand">
      <p class="brand__name">Ridgeline Valley</p>
      <p class="brand__tagline">HOMES</p>
    </div>
    <div class="sign__edge sign__edge--bottom"></div>
  </main>
</body>
</html>
```